Banner Ad Designs for tick and flea products

We sell tick and flea products online and want some great banner designs for our online website to promote our tick and flea products.

The ads must be made up in both Flash and HTML5
Ads can be formatted as .JPEG or .GIF files.

Please see the following url for creative requirements
http://help.bannerquay.com/creative-requirements/

Creative licence no limits to your imagination!

Ads must be created in the following sizes:

- Banner – 468×60
- Square – 250×250
- Small Square – 200×200
- Leaderboard – 728×90
- Medium Rectangle – 300×250
- Chatterbox – 100×72

please view our website at www.harbourlanepawstore.com.au or .com to get a feel for our website.

The aim is to attract customers who want to save on tick and flea purchases for their pets (dogs and cats)

Target Market(s)

Anyone who owns a dog or cat

Industry/Entity Type

Online

Font styles to use
Sans Serif
Other font styles liked:
• creative licence on font styles

Requirements
Must have
• Must have a strong urge to entice customers to click through.

Images wording and text etc use creative lic
Nice to have
• Strong appeal to dog and cat owners and how they can save on flea and tick essentials.
Keep it simple but effective.
Be fun and playful and inviting.
Should not have
• Please do not use words like cheap - cheapest

Strobing & Flashing - Strobing, flashing backgrounds, or otherwise distracting ads are not allowed. Do not attempt to overtly distract the user from page content.

```html
<!DOCTYPE html>
<html lang="en">
<head>
<meta charset="utf-8">
<title>Harbour Lane Paw Store – Tick &amp; Flea Banner Concepts</title>
<link rel="stylesheet" href="https://fonts.googleapis.com/css2?family=Federo&family=Roboto+Condensed:wght@400;700&display=swap">
<style>
  :root {
    --page: #ffffff;
    --board: #6d6d6d;
    --label: #111111;
    --green: #86ae34;
    --green-light: #a9c96d;
    --green-pale: #c8dca1;
    --white: #ffffff;
    --ink: #1f2d4a;
    --btn-top: #8ae45a;
    --btn-bottom: #23a028;
    --btn-edge: #1a6e1e;
    --btn-text: #f6f200;
    --photo-dark: #7a5a3e;
    --photo-mid: #b99a78;
    --photo-light: #e9dccb;
  }
  html, body {
    margin: 0;
    width: 1200px;
    height: 900px;
    overflow: hidden;
    background: var(--page);
  }
  .canvas {
    position: relative;
    width: 1200px;
    height: 900px;
  }
  .board {
    position: absolute;
    left: 0;
    top: 94px;
    width: 1200px;
    height: 652px;
    background: var(--board);
  }
  .variant-label {
    position: absolute;
    left: 8px;
    font-family: "Roboto Condensed", Arial, sans-serif;
    font-weight: 400;
    font-size: 56px;
    line-height: 1;
    color: var(--label);
  }
  .banner {
    position: absolute;
    width: 1091px;
    height: 134px;
    background: var(--green);
    overflow: hidden;
  }
  .banner-shapes {
    position: absolute;
    inset: 0;
  }
  .pet-photo {
    position: absolute;
    top: 6px;
    width: 170px;
    height: 122px;
    border-radius: 50%;
  }
  .pet-photo--left {
    left: 4px;
    background: radial-gradient(ellipse at 45% 50%, var(--photo-dark) 0%, var(--photo-mid) 45%, var(--photo-light) 72%, rgba(255,255,255,0) 100%);
  }
  .pet-photo--right {
    right: 4px;
    width: 180px;
    background: radial-gradient(ellipse at 55% 50%, var(--photo-mid) 0%, var(--photo-light) 60%, rgba(255,255,255,0) 100%);
  }
  .headline {
    position: absolute;
    margin: 0;
    font-family: "Federo", "Century Gothic", sans-serif;
    font-weight: 400;
    color: var(--white);
    text-align: center;
    white-space: nowrap;
  }
  .headline--two-line {
    left: 184px;
    width: 560px;
    top: 20px;
    font-size: 43px;
    line-height: 50px;
    letter-spacing: 1.5px;
  }
  .headline--single {
    left: 217px;
    width: 640px;
    top: 34px;
    font-size: 56px;
    line-height: 64px;
    letter-spacing: 2px;
  }
  .headline--with-cta {
    left: 250px;
    width: 440px;
    top: 4px;
    font-size: 50px;
    line-height: 60px;
    letter-spacing: 2px;
  }
  .order-button {
    position: absolute;
    left: 371px;
    top: 72px;
    width: 196px;
    height: 49px;
    box-sizing: border-box;
    border: 2px solid var(--btn-edge);
    border-radius: 6px;
    background: linear-gradient(to bottom, var(--btn-top), var(--btn-bottom));
    font-family: "Roboto Condensed", Arial, sans-serif;
    font-weight: 700;
    font-size: 28px;
    line-height: 45px;
    text-align: center;
    color: var(--btn-text);
    text-decoration: none;
    letter-spacing: -0.5px;
  }
  .brand {
    position: absolute;
    left: 842px;
    top: 0;
    height: 134px;
    display: flex;
    align-items: center;
    gap: 12px;
  }
  .brand-dot {
    flex: none;
    width: 46px;
    height: 46px;
    border-radius: 50%;
    background: var(--ink);
  }
  .brand-name {
    font-family: "Federo", "Century Gothic", sans-serif;
    font-weight: 400;
    font-size: 28px;
    line-height: 34px;
    color: var(--ink);
    white-space: nowrap;
  }
</style>
</head>
<body>
<div class="canvas">
  <div class="board"></div>

  <span class="variant-label" style="top:212px;">A</span>
  <div class="banner" style="left:70px; top:186px;">
    <svg class="banner-shapes" width="1091" height="134" viewBox="0 0 1091 134" aria-hidden="true">
      <path d="M0 0 H160 Q205 67 160 134 H0 Z" fill="var(--white)"/>
      <path d="M790 0 Q752 67 790 134 H1091 V0 Z" fill="var(--green-light)"/>
      <path d="M812 0 Q774 67 812 134 H1091 V0 Z" fill="var(--green-pale)"/>
      <path d="M834 0 Q796 67 834 134 H1091 V0 Z" fill="var(--white)"/>
    </svg>
    <div class="pet-photo pet-photo--left" role="img" aria-label="Photo of a small dog and a tabby cat lying together"></div>
    <p class="headline headline--two-line">Save on genuine brand<br>tick and flea products</p>
    <div class="brand">
      <span class="brand-dot"></span>
      <span class="brand-name">Harbour Lane<br>Paw Store</span>
    </div>
  </div>

  <span class="variant-label" style="top:382px;">B</span>
  <div class="banner" style="left:70px; top:355px;">
    <svg class="banner-shapes" width="1091" height="134" viewBox="0 0 1091 134" aria-hidden="true">
      <path d="M0 0 H160 Q205 67 160 134 H0 Z" fill="var(--white)"/>
      <path d="M930 0 Q885 67 930 134 H1091 V0 Z" fill="var(--white)"/>
    </svg>
    <div class="pet-photo pet-photo--left" role="img" aria-label="Photo of a small dog and a tabby cat lying together"></div>
    <p class="headline headline--single">Protect Your Pets!</p>
    <div class="pet-photo pet-photo--right" role="img" aria-label="Photo of two pug dogs side by side"></div>
  </div>

  <span class="variant-label" style="top:560px;">C</span>
  <div class="banner" style="left:67px; top:532px;">
    <svg class="banner-shapes" width="1091" height="134" viewBox="0 0 1091 134" aria-hidden="true">
      <path d="M0 0 H160 Q205 67 160 134 H0 Z" fill="var(--white)"/>
      <path d="M790 0 Q752 67 790 134 H1091 V0 Z" fill="var(--green-light)"/>
      <path d="M812 0 Q774 67 812 134 H1091 V0 Z" fill="var(--green-pale)"/>
      <path d="M834 0 Q796 67 834 134 H1091 V0 Z" fill="var(--white)"/>
    </svg>
    <div class="pet-photo pet-photo--left" role="img" aria-label="Photo of a small dog and a tabby cat lying together"></div>
    <p class="headline headline--with-cta">Save with us</p>
    <a class="order-button" href="#">ORDER NOW</a>
    <div class="brand">
      <span class="brand-dot"></span>
      <span class="brand-name">Harbour Lane<br>Paw Store</span>
    </div>
  </div>
</div>
</body>
</html>
```